Reed diffusers - packing design

Dear Sir/Madam,

For this project, we would like to come up with a different style of product packing design for our reed diffuser Mandarin 100ml.

Important:

The text on the box should remain the same, the logo should be positioned on the same location and it is very important to keep the text ‘’Reed diffuser’’ and the type of fragrance on the front of the packing.

This are the key and main keywords for the positions, and the customer must identify the product and relate to fragrance.
Besides that, we can think of any kind of graphic design style.

We are trying to advertise/sell a smell/scent
It brings you back to a place/memory/experience and can be displayed/visualized in form of an image or icon (natural/organic) in order to express a feeling or an emotion which a potential customer can relate

We follow the strategy of applying matching colors (for the scent variations) on the main page and we want to identify colors which are not used by competitors (USP)

The packaging itself should be perceived as a gift box and should have a luxury touch
On the package itself - it should be included a hint of the most common locations which are likely used for a “Reed Diffuser” (Comfort room, Living room) associated in form of a pattern or icons.

Font: Adobe Garamond Pro en Arial

With kind regards,

```html
<!DOCTYPE html>
<html lang="en">
<head>
<meta charset="utf-8">
<title>Reed diffuser Mandarin – gift box dieline</title>
<link rel="stylesheet" href="https://fonts.googleapis.com/css2?family=EB+Garamond:ital,wght@0,400;0,600;1,400&family=Arimo:wght@400;700&display=swap">
<style>
  :root{
    --paper:#ffffff;
    --cream:#fdf7ee;
    --bg:#f4f1ec;
    --orange:#f29a2e;
    --orange-deep:#e0781c;
    --gold:#c9a25a;
    --ink:#3a2e22;
    --muted:#6d5f50;
    --line:#e9a24a;
    --warn:#d6221c;
  }
  html,body{margin:0;padding:0;overflow:hidden;background:var(--bg);}
  .canvas{position:relative;width:791px;height:1200px;overflow:hidden;background:var(--bg);font-family:"Arimo",Arial,sans-serif;color:var(--ink);}
  .dieline{position:absolute;inset:0;}
  .panel{position:absolute;background:var(--paper);box-sizing:border-box;}
  .copy{font-size:7.2px;line-height:1.4;color:var(--muted);}
  .copy p{margin:0 0 6px;}
  .copy b{color:var(--ink);}
  .panel-back{left:100px;top:130px;width:185px;height:920px;padding:18px 14px;}
  .panel-front{left:285px;top:130px;width:243px;height:920px;text-align:center;background:var(--cream);}
  .front-frame{position:absolute;inset:8px;border:1px solid var(--gold);pointer-events:none;}
  .front-frame::after{content:"";position:absolute;inset:3px;border:0.5px solid var(--gold);}
  .panel-nl{left:528px;top:130px;width:132px;height:920px;padding:60px 10px 18px;}
  .panel-side{left:660px;top:130px;width:105px;height:920px;padding:14px 8px;}
  .redact{width:80px;height:30px;background:#111;margin-bottom:14px;}
  .brand{font-family:"EB Garamond",Georgia,serif;font-weight:600;color:var(--orange-deep);letter-spacing:2px;}
  .brand-front{font-size:15px;margin-top:6px;}
  .brand-dot{display:block;margin:18px auto 0;width:44px;height:44px;border-radius:50%;border:2px solid var(--orange);}
  .fruit{margin:12px auto 0;width:196px;height:162px;border-radius:8px;background:radial-gradient(circle at 40% 45%,#f7a83a,#ec7b1a 60%,#6ea345 100%);}
  .product{margin:34px auto 0;width:110px;height:330px;background:linear-gradient(180deg,#fdf7ee 0%,#f3eee8 40%,#c9b2a8 100%);border-radius:6px;}
  .title-sm{font-family:"EB Garamond",Georgia,serif;font-size:19px;color:var(--orange-deep);margin-top:18px;}
  .title{font-family:"EB Garamond",Georgia,serif;font-size:38px;line-height:1;color:var(--orange-deep);}
  .subtitle{font-family:"EB Garamond",Georgia,serif;font-style:italic;font-size:11px;color:var(--ink);margin-top:4px;}
  .rooms{display:flex;justify-content:center;gap:22px;margin-top:22px;}
  .room{display:flex;flex-direction:column;align-items:center;gap:4px;font-size:6.5px;letter-spacing:1px;text-transform:uppercase;color:var(--gold);}
  .room svg{stroke:var(--gold);fill:none;stroke-width:1.3;}
  .warn-row{display:flex;gap:8px;margin-top:20px;}
  .side-fruit{width:86px;height:70px;border-radius:6px;margin:8px 0 10px;background:radial-gradient(circle,#f7a83a,#ec7b1a 70%,#6ea345);}
  .side-rooms{display:flex;flex-direction:column;gap:10px;margin-top:16px;}
  .side-rooms svg{stroke:var(--gold);fill:none;stroke-width:1.2;}
  .batch{position:absolute;left:8px;bottom:16px;}
</style>
</head>
<body>
<div class="canvas">
  <svg class="dieline" width="791" height="1200" viewBox="0 0 791 1200" aria-hidden="true">
    <g fill="var(--orange)" stroke="var(--line)" stroke-width="1">
      <path d="M100 130 L110 70 L275 70 L285 130 Z"/>
      <path d="M285 130 L295 20 L518 20 L528 130 Z"/>
      <path d="M528 130 L538 75 L650 75 L660 130 Z"/>
      <path d="M660 130 L668 40 L757 40 L765 130 Z"/>
      <path d="M100 1050 L110 1110 L275 1110 L285 1050 Z"/>
      <path d="M285 1050 L295 1180 L518 1180 L528 1050 Z"/>
      <path d="M528 1050 L538 1105 L650 1105 L660 1050 Z"/>
      <path d="M660 1050 L668 1140 L757 1140 L765 1050 Z"/>
      <path d="M100 140 L78 160 L78 1020 L100 1040 Z"/>
    </g>
    <circle cx="128" cy="95" r="16" fill="none" stroke="var(--paper)" stroke-width="1.5"/>
    <g stroke="var(--paper)" stroke-width="1" fill="none" opacity="0.8">
      <line x1="300" y1="60" x2="513" y2="60"/>
      <line x1="300" y1="1140" x2="513" y2="1140"/>
    </g>
    <g stroke="var(--line)" stroke-width="1" fill="none">
      <rect x="100" y="130" width="665" height="920"/>
      <line x1="285" y1="130" x2="285" y2="1050"/>
      <line x1="528" y1="130" x2="528" y2="1050"/>
      <line x1="660" y1="130" x2="660" y2="1050"/>
    </g>
  </svg>

  <section class="panel panel-back copy">
    <div class="redact"></div>
    <p><b>Oil de Citrina – Aroma Reed Diffuser Mandarin with bamboo sticks.</b></p>
    <p>Natural mandarin essential oil, which is part of the aroma composition, spreads a fresh citrus scent through the room, has a beneficial health effect, lifts your spirits and helps to breathe easily. It is the perfect fragrance for a productive and relaxing atmosphere.</p>
    <p><b>Application:</b> for room air aromatization.</p>
    <p><b>Method of application:</b> open the bottle, insert bamboo sticks into the bottle and turn them over regularly. The intensity of the scent depends on the number of sticks used.</p>
    <p><b>Ingredients:</b> PEG, Dihexyl Ether, Citrus Reticulata Peel Oil.</p>
    <p><b>Storage conditions:</b> for external use. Keep out of reach of children. Avoid contact with eyes and skin. Store at room temperature away from direct sunlight and open flame.</p>
    <p><b>Produced for:</b><br>Citrina Home BV, Lindelaan 12,<br>1234 AB Voorbeeld, Nederland<br>hello@citrina-home.nl<br>www.citrina-home.nl</p>
    <p><b>Nominal volume:</b> 100 ml</p>
    <div class="warn-row">
      <svg width="40" height="40" viewBox="0 0 40 40" aria-hidden="true"><rect x="8" y="8" width="24" height="24" transform="rotate(45 20 20)" fill="#fff" stroke="var(--warn)" stroke-width="3"/><line x1="20" y1="12" x2="20" y2="23" stroke="#111" stroke-width="3"/><circle cx="20" cy="28" r="2" fill="#111"/></svg>
      <svg width="40" height="40" viewBox="0 0 40 40" aria-hidden="true"><rect x="8" y="8" width="24" height="24" transform="rotate(45 20 20)" fill="#fff" stroke="var(--warn)" stroke-width="3"/><path d="M12 26 H28" stroke="#111" stroke-width="2"/><path d="M16 22 Q20 14 24 22" stroke="#111" stroke-width="2" fill="none"/></svg>
    </div>
  </section>

  <section class="panel panel-front">
    <div class="front-frame"></div>
    <span class="brand-dot"></span>
    <div class="brand brand-front">CITRINA</div>
    <div class="fruit" role="img" aria-label="Illustration of two ripe mandarins with green leaves"></div>
    <div class="product" role="img" aria-label="Photo of a glass reed diffuser bottle with bamboo sticks"></div>
    <div class="title-sm">Reed diffuser</div>
    <div class="title">Mandarin</div>
    <div class="subtitle">with natural mandarin essential oil</div>
    <div class="rooms">
      <div class="room">
        <svg width="26" height="20" viewBox="0 0 26 20" aria-hidden="true"><path d="M3 10 V16 H23 V10"/><path d="M6 10 V6 H20 V10"/><path d="M3 10 H23"/><path d="M5 16 V19 M21 16 V19"/></svg>
        Living room
      </div>
      <div class="room">
        <svg width="26" height="20" viewBox="0 0 26 20" aria-hidden="true"><path d="M2 10 H24"/><path d="M4 10 V14 Q4 17 8 17 H18 Q22 17 22 14 V10"/><path d="M6 10 V3 Q6 1 9 1 V3"/><path d="M8 17 V19 M18 17 V19"/></svg>
        Comfort room
      </div>
    </div>
  </section>

  <section class="panel panel-nl copy">
    <p><b>Oil Geurstokjes Diffuser Mandarijn met bamboe stokjes.</b></p>
    <p>De natuurlijke mandarijnolie in de geurcompositie verspreidt een frisse citrusgeur door de kamer, werkt verkwikkend, verbetert de stemming en helpt vrij te ademen. De perfecte geur voor een productieve en ontspannen sfeer.</p>
    <p><b>Toepassing:</b> voor het geuren van ruimtes.</p>
    <p><b>Gebruiksaanwijzing:</b> open het flesje, plaats de bamboe stokjes en draai ze regelmatig om. De intensiteit hangt af van het aantal stokjes.</p>
    <p><b>Ingrediënten:</b> PEG, Dihexyl Ether, Citrus Reticulata Peel Oil.</p>
    <p><b>Bewaren:</b> buiten bereik van kinderen. Vermijd contact met ogen en huid. Bewaren op kamertemperatuur, uit direct zonlicht.</p>
    <p><b>Gemaakt voor:</b><br>Citrina Home BV, Lindelaan 12,<br>1234 AB Voorbeeld<br>hello@citrina-home.nl</p>
    <p><b>Inhoud:</b> 100 ml</p>
  </section>

  <section class="panel panel-side copy">
    <span class="brand-dot" style="margin:0 0 4px;width:30px;height:30px"></span>
    <div class="brand" style="font-size:9px">CITRINA</div>
    <div class="side-fruit" role="img" aria-label="Small mandarin illustration"></div>
    <p><b>Reed diffuser Mandarin</b><br>100 ml</p>
    <div class="side-rooms">
      <svg width="26" height="20" viewBox="0 0 26 20" aria-hidden="true"><path d="M3 10 V16 H23 V10"/><path d="M6 10 V6 H20 V10"/><path d="M3 10 H23"/><path d="M5 16 V19 M21 16 V19"/></svg>
      <svg width="26" height="20" viewBox="0 0 26 20" aria-hidden="true"><path d="M2 10 H24"/><path d="M4 10 V14 Q4 17 8 17 H18 Q22 17 22 14 V10"/><path d="M6 10 V3 Q6 1 9 1 V3"/><path d="M8 17 V19 M18 17 V19"/></svg>
    </div>
    <p class="batch">Batch no.<br>Best before</p>
  </section>
</div>
</body>
</html>
```